Improve Design and Readability of Existing Web Page

Corvantia.org is a free educational radiology resource with one of the web's largest collections of radiology cases and reference articles. This job involves improving the design of the article pages to make the text more readable.
We want a new design for the body of the article page that has considered at least: the typeface, vertical rhythm, line length, line height and styling of the text, headings and other standard HTML elements. IMPORTANT: You would only be designing the content area of the page, inside the existing layout, as indicated here: http://q.zx/i/Tk4W
If you are the successful applicant you'll have your work featured across the 6000+ article pages on the site.
The HTML elements that you will need to consider in your design are:
* Headings (three levels)
* Paragraphs
* Superscript and Subscript text
* Ordered and unordered lists, potentially nested multiple levels deep
* Links to other corvantia content (blue links)
* Links to other corvantia content that does not yet exist (grey links)
The articles are accessible at: http://corvantia.org/encyclopaedia/all/all
Sample articles that can be used for reference and as a base for the redesign:
* http://corvantia.org/articles/neurosarcoidosis
* http://corvantia.org/articles/golden_s_sign
* http://corvantia.org/articles/fetal-heart-rate
* http://corvantia.org/articles/meningioma

```html
<!DOCTYPE html>
<html lang="en">
<head>
<meta charset="utf-8">
<title>Neurosarcoidosis – Corvantia.org</title>
<link href="https://fonts.googleapis.com/css2?family=PT+Sans:wght@400;700&family=Arimo:wght@400;700&display=swap" rel="stylesheet">
<style>
:root{
  --ink:#000;
  --navy:#1d1f4a;
  --navy-deep:#121433;
  --purple:#3b1f6b;
  --tab:#2c2e6a;
  --tab-blue:#27468f;
  --link:#1f2f8c;
  --heading:#213a86;
  --text:#555;
  --accent-blue:#1a9be0;
  --side:#e4e4e4;
  --orange:#f07a1c;
  --white:#fff;
  --bullet:#3a2a6e;
}
*{box-sizing:border-box;margin:0;padding:0}
html,body{width:1026px;height:1200px;overflow:hidden;background:var(--ink)}
.page{position:relative;width:1104px;height:1291px;transform:scale(0.9293);transform-origin:0 0;font-family:"PT Sans",sans-serif;background:var(--ink)}
.abs{position:absolute}
.header{left:60px;top:0;width:986px;height:271px;background:linear-gradient(180deg,#1a1c3e 0%,#262a62 55%,#2f2f70 100%)}
.brand{left:82px;top:28px;display:flex;align-items:center;gap:8px;color:var(--white);font-family:"Arimo",sans-serif;font-size:30px;font-weight:700;letter-spacing:-1px}
.brand-mark{width:38px;height:38px;background:#6b7fd8;border-radius:4px}
.network{left:328px;top:54px;color:#fff;font-family:"Arimo",sans-serif;font-size:13px;display:flex;align-items:center;gap:8px}
.network .dot{width:22px;height:22px;border-radius:50%;background:#fff}
.account{left:910px;top:14px;font-family:"Arimo",sans-serif;font-size:11px;color:#ddd}
.ad{left:190px;top:101px;width:728px;height:90px;background:#000;color:#fff;font-family:"Arimo",sans-serif}
.ad-brand{position:absolute;left:22px;top:22px;color:#e0141a;font-size:21px;font-weight:700}
.ad-tag{position:absolute;left:22px;top:46px;font-size:12px;font-weight:700}
.ad-figure{position:absolute;left:215px;top:0;width:70px;height:90px;background:linear-gradient(180deg,#777,#2a4fd0 70%,#555)}
.ad-title{position:absolute;left:344px;top:6px;font-size:22px;font-weight:700;font-style:italic;line-height:22px;color:#f0c419}
.ad-title span{color:#35c6e8}
.ad-copy{position:absolute;left:345px;top:54px;font-size:12px;font-style:italic}
.ad-more{position:absolute;left:345px;top:70px;font-size:10px;font-style:italic;color:#e0141a}
.ads-note{left:836px;top:196px;font-family:"Arimo",sans-serif;font-size:10px;color:#aab;text-decoration:underline}
.tab{top:214px;height:57px;background:var(--tab);color:#fff;font-family:"Arimo",sans-serif;font-weight:700;padding:16px 0 0 16px;font-size:14px}
.tab small{display:block;font-weight:400;font-size:8px;color:#8a8cb8;margin-top:2px}
.tab.blue{background:var(--tab-blue)}
.tab.add{font-size:12px;line-height:12px;padding:16px 0 0 38px}
.tab.add::before{content:"+";position:absolute;left:14px;top:14px;font-size:22px}
.tab.quiz::before{content:"?";left:16px}
.search{left:731px;top:220px;width:292px;height:50px;background:#323471}
.search-field{position:absolute;left:10px;top:12px;width:204px;height:23px;background:#3d4080}
.search-btn{position:absolute;left:224px;top:12px;width:58px;height:24px;background:#111;color:#fff;font:700 11px "Arimo",sans-serif;text-align:center;line-height:24px;border-radius:3px}
.sidebar{left:636px;top:271px;width:404px;height:827px;background:var(--side)}
.article{left:67px;top:271px;width:569px;height:828px;background:#fff;border:3px solid var(--accent-blue);padding:24px 24px 0 24px;color:var(--text)}
.article h1{font-size:28px;font-weight:400;color:var(--heading);line-height:32px}
.byline{font-size:12px;color:#3b66b8;margin-top:3px;padding-bottom:12px;border-bottom:1px solid #e2e2e2;width:504px}
.article p{font-size:13.3px;line-height:22px;margin-top:10px;width:512px}
.article p.lead{margin-top:18px}
.article a{color:var(--link);text-decoration:none}
.article h2{font-size:22px;font-weight:400;color:var(--heading);margin-top:30px;line-height:26px}
.article h2 + p{margin-top:5px}
sup{font-size:9px;line-height:0}
ul.points{list-style:none;margin-top:16px;margin-left:14px}
ul.points>li{position:relative;padding-left:28px;font-size:13px;color:var(--link);line-height:20px;margin-bottom:8px}
ul.points>li::before{content:"›";position:absolute;left:0;top:0;width:20px;height:20px;border-radius:50%;background:var(--bullet);color:#fff;font-size:16px;line-height:17px;text-align:center;font-weight:700}
ul.sub{list-style:none;margin-top:8px;margin-left:-18px}
ul.sub li{padding-left:10px;position:relative;line-height:22px;color:#3b66b8}
ul.sub li::before{content:"›";position:absolute;left:0;color:#999}
.tools{left:653px;top:286px;width:368px;height:46px;background:#fff;border:1px solid #3a4a9a;border-radius:3px}
.btn{position:absolute;top:10px;height:24px;border:1px solid #bbb;border-radius:3px;background:linear-gradient(#fff,#e8e8e8);font:11px "Arimo",sans-serif;color:#333;line-height:22px;text-align:center}
.info{left:655px;top:347px;width:365px;height:85px;background:#f3f3f3;border-radius:3px}
.info-head{height:38px;background:var(--navy);color:#fff;font:700 12px "Arimo",sans-serif;padding:12px 16px;border-radius:3px 3px 0 0}
.info-row{margin:8px 10px;background:#fff;height:26px;padding:6px 11px;font:11px "Arimo",sans-serif;color:#333}
.info-row b{font-weight:700}
.info-row a{color:#2050c0;text-decoration:underline}
.promo{left:688px;top:447px;width:300px;height:250px;background:#111;border:1px solid #444}
.promo-head{height:42px;background:linear-gradient(#4a2a7a,#351c5e);color:#fff;font:21px "Arimo",sans-serif;padding:8px 20px}
.shot{position:absolute;top:76px;width:82px;height:76px;background:radial-gradient(#bbb,#333)}
.promo-line{position:absolute;left:0;width:100%;top:172px;text-align:center;color:#fff;font:13px "Arimo",sans-serif}
.promo-btn{position:absolute;left:34px;top:202px;width:232px;height:31px;background:linear-gradient(#f7912c,#e46a0e);color:#fff;font:11px "Arimo",sans-serif;text-align:center;line-height:31px;border-radius:2px}
.bands{left:67px;top:1098px;width:973px;height:7px;background:linear-gradient(90deg,#2b2f7a,#5b2a8a 30%,#2b4a9a 55%,#6a3a9a 80%,#3a5aa0)}
.footer{left:67px;top:1118px;width:973px;height:155px;background:#222}
.cta{left:188px;top:1132px;width:727px;height:89px;background:radial-gradient(circle at 60% 40%,#5a5ab0,#26266a 70%);border:1px solid #555;color:#fff;font-family:"Arimo",sans-serif}
.cta h3{position:absolute;left:17px;top:8px;font-size:29px;font-weight:700}
.cta p{position:absolute;left:19px;top:50px;font-size:20px;color:#ddd}
.cta-btn{position:absolute;left:594px;top:29px;width:116px;height:34px;background:linear-gradient(#f8b12a,#ef8a12);font-size:13px;font-weight:700;text-align:center;line-height:34px;border-radius:3px}
.foot-links{left:67px;top:1236px;width:973px;height:37px;background:#1a1a1a;border-top:1px solid #333;font:700 12px "Arimo",sans-serif;color:#ddd}
.foot-links span{position:absolute;top:11px}
</style>
</head>
<body>
<div class="page">
  <header class="abs header"></header>
  <div class="abs brand"><span class="brand-mark"></span>Corvantia.org</div>
  <div class="abs network">Member of the <span class="dot"></span> Helden Medica network</div>
  <div class="abs account">Log in &nbsp;|&nbsp; Sign up</div>

  <div class="abs ad">
    <div class="ad-brand">NORVIKA</div>
    <div class="ad-tag">Leading Innovation »»</div>
    <div class="ad-figure" role="img" aria-label="Scanner figure with dose colour map"></div>
    <div class="ad-title">NEW DOSE<br><span>TRACKING SYSTEM</span></div>
    <div class="ad-copy">Just one of Norvika's 41 dose saving features available</div>
    <div class="ad-more">Click here to get the full story</div>
  </div>
  <div class="abs ads-note">About these ads</div>

  <nav>
    <div class="abs tab" style="left:82px;width:149px">ENCYCLOPEDIA<small>(Browse by topic or system)</small></div>
    <div class="abs tab add" style="left:233px;width:90px">Add<br>Article</div>
    <div class="abs tab blue" style="left:331px;width:151px">PATIENT CASES<small>(Browse by topic or system)</small></div>
    <div class="abs tab blue add" style="left:484px;width:90px">Add<br>Case</div>
    <div class="abs tab blue add quiz" style="left:576px;width:90px">Quiz<br>Mode</div>
    <div class="abs search"><div class="search-field"></div><div class="search-btn">Search</div></div>
  </nav>

  <aside class="abs sidebar"></aside>

  <article class="abs article">
    <h1>Neurosarcoidosis</h1>
    <div class="byline">Dr Alan Pryce and Dr Martin Velloch et al.</div>
    <p class="lead"><a href="#">Central nervous system involvement by sarcoidosis</a> (also termed <a href="#">neurosarcoidosis</a>) is relatively common among patients with systemic <a href="#">sarcoidosis</a> and has a bewildering variety of manifestions, often making diagnosis difficult.</p>
    <p>For a general discussion of the underlying condition, please refer to the article <a href="#">sarcoidosis.</a></p>
    <h2>Epidemiology</h2>
    <p>The demographics of affected patients is not different to that of systemic sarcoidosis, typically affecting patients 30-40 years of age with a female predilection<sup>2</sup>. Histologically, central nervous system involvement is seen in 14-27% of patients with systemic sarcoidosis, although only 3-15% are symptomatic<sup>1-3</sup>. Interestingly up to 10% of patients with systemic disease will demonstrate imaging findings; thus not all patients with demonstrable imaging findings of neurosarcoidosis are symptomatic.</p>
    <h2>Clinical presentation</h2>
    <p>Central nervous system involvement by sarcoidosis is very variable, with lesions potentially involving the leptomeninges, pituitary and parenchyma of all parts of the intracranial compartment. Thus clinical presentation is also vary variable and non-specific. It includes:</p>
    <ul class="points">
      <li>Signs and symptoms of raised ICP due to hydrocephalus.</li>
      <li>Cranial nerve palsies.
        <ul class="sub"><li>Optic nerve involvement (particularly common)<sup>5</sup></li><li>Facial nerve pals</li></ul>
      </li>
      <li>Diabetes insipidus from pituitary involvement</li>
      <li>Seizures</li>
      <li>Variable weakness, paresthesias and dysarthria / dysphasia</li>
      <li>Spinal cord involvement presenting as myelopathy<sup>5</sup></li>
    </ul>
  </article>

  <div class="abs tools">
    <div class="btn" style="left:11px;width:94px">✎ Edit Article</div>
    <div class="btn" style="left:115px;width:62px">Share ▾</div>
    <div class="btn" style="left:187px;width:45px">⚙▾</div>
  </div>
  <div class="abs info">
    <div class="info-head">Article Information:</div>
    <div class="info-row"><b>Section:</b> <a href="#">Physics</a></div>
  </div>
  <div class="abs promo">
    <div class="promo-head">Corvantia.org Orbit app</div>
    <div class="shot" role="img" aria-label="Abdominal CT slice" style="left:12px"></div>
    <div class="shot" role="img" aria-label="Coronal CT image" style="left:108px"></div>
    <div class="shot" role="img" aria-label="Axial abdominal CT" style="left:204px"></div>
    <div class="promo-line">New case packs every month</div>
    <div class="promo-btn">CLICK TO FIND OUT MORE</div>
  </div>

  <div class="abs bands"></div>
  <footer class="abs footer"></footer>
  <div class="abs cta">
    <h3>With over 12,000 cases</h3>
    <p>Isn't it time you started... ‘cos it will take you some time....</p>
    <div class="cta-btn">GET STARTED</div>
  </div>
  <div class="abs foot-links">
    <span style="left:16px">Encyclopaedia</span>
    <span style="left:506px">Patient Cases</span>
    <span style="left:836px">About Corvantia.org</span>
  </div>
</div>
</body>
</html>
```